Retail Appliance Store Chain needs NEW business Card

Name of my company is Brandon's Appliances brandonsappliances.com is our website. . We are a 2 location brick and mortar, and online store selling premium, luxury, and normal household appliances, such as ovens, stoves, cooktops, dishwashers, refrigerators, washers and dryers, grills, air conditioners etc. The focus is on large kitchen appliances and laundry appliances.
Please visit http://brandonsappliances.com to get a feel for the business and branding.
I have attached the Brandon's Appliances logo (i do not have eps or psd or ai). And I have also attached our current business cards that we use. We have two versions. A double sided version for managers, and a one side version for regular employees.
Please submit BOTH one sided and two sided designs if possible.
Please keep consistent with the Brandon's Appliances logo, colors, etc.
I would prefer no rounded corners on the business card designs for printing costs.
Information on the cards (in no particular order):
Name - Employee Name
Business name - Brandon's Appliances
website - brandonsappliances.com
Email - Employee Email
2 Phone Numbers - store 1 address, store 2 address
2 Addresses - store 1 address, store 2 address

*do NOT need Fax #

Industry/Entity Type

Home Appliance

Contact Information for Business Card

Logo - Brandons Appliances Logo
Name - Employee Name
Email - Employee Email

Please no rounded corners. Standard US Business Card Size please.

Font styles to use
Serif
Sans Serif

Requirements
Must have
• colors and design that somewhat match the feel of current logo and website
Should not have
• No rounded corners.
No non-traditional business card size. US Standard Business Card Size only

```html
<!DOCTYPE html>
<html lang="en">
<head>
<meta charset="utf-8">
<title>Brandon's Appliances – Business Cards</title>
<link rel="stylesheet" href="https://fonts.googleapis.com/css2?family=Montserrat:wght@400;500;800&display=swap">
<style>
  :root {
    --brand-blue: #2f64a8;
    --paper: #ffffff;
    --backdrop: #e9ebef;
    --ink-soft: #4a4f57;
  }
  * { box-sizing: border-box; margin: 0; padding: 0; }
  html, body { width: 1200px; height: 800px; overflow: hidden; }
  body {
    background: var(--backdrop);
    font-family: "Montserrat", Arial, sans-serif;
    position: relative;
  }
  .card {
    position: absolute;
    top: 250px;
    width: 525px;
    height: 300px;
    background: var(--paper);
    overflow: hidden;
    box-shadow: 0 6px 18px rgba(0,0,0,0.12);
  }
  .card--front { left: 50px; }
  .card--back { left: 625px; }
  .card__waves { position: absolute; inset: 0; width: 100%; height: 100%; }
  .wave { fill: var(--brand-blue); }

  .brand-name {
    position: absolute;
    font-weight: 800;
    line-height: 1.05;
    letter-spacing: 0.01em;
  }
  .card--front .brand-name {
    top: 56px; right: 140px;
    width: 150px;
    text-align: right;
    font-size: 21px;
    color: var(--brand-blue);
  }
  .card--back .brand-name {
    top: 82px; left: 120px;
    font-size: 30px;
    color: var(--paper);
  }

  .employee {
    position: absolute;
    left: 38px; top: 128px;
  }
  .employee__name {
    font-size: 21px;
    font-weight: 800;
    color: var(--brand-blue);
    margin-bottom: 14px;
  }
  .contact-list { list-style: none; }
  .contact-list li {
    display: flex;
    align-items: center;
    gap: 9px;
    font-size: 9.5px;
    color: var(--ink-soft);
    margin-bottom: 6px;
  }
  .contact-list svg { width: 10px; height: 10px; fill: var(--brand-blue); flex: none; }

  .website {
    position: absolute;
    right: 50px; bottom: 44px;
    font-size: 10px;
    font-weight: 500;
    letter-spacing: 0.22em;
    color: var(--brand-blue);
  }
</style>
</head>
<body>

  <section class="card card--front" aria-label="Business card front">
    <svg class="card__waves" viewBox="0 0 525 300" aria-hidden="true">
      <path class="wave" d="M0 0 H70 C40 15 20 30 0 40 Z"/>
      <path class="wave" d="M525 40 C470 70 440 120 415 170 C470 110 500 95 525 90 Z"/>
      <path class="wave" d="M525 110 C470 130 440 190 410 260 C380 290 340 300 300 300 H525 Z"/>
      <path class="wave" d="M0 248 C140 282 280 265 390 200 C300 270 180 290 0 292 Z"/>
    </svg>
    <div class="brand-name">Brandon's Appliances</div>
    <div class="employee">
      <h1 class="employee__name">JORDAN HALE</h1>
      <ul class="contact-list">
        <li>
          <svg viewBox="0 0 24 24"><path d="M6.6 10.8a15.1 15.1 0 0 0 6.6 6.6l2.2-2.2a1 1 0 0 1 1-.25 11.4 11.4 0 0 0 3.6.57 1 1 0 0 1 1 1V20a1 1 0 0 1-1 1A17 17 0 0 1 3 4a1 1 0 0 1 1-1h3.5a1 1 0 0 1 1 1c0 1.25.2 2.45.57 3.57a1 1 0 0 1-.25 1z"/></svg>
          (555) 014-2023
        </li>
        <li>
          <svg viewBox="0 0 24 24"><path d="M2 5h20v14H2z M4 7v.5l8 5 8-5V7l-8 5z" fill-rule="evenodd"/></svg>
          jordanh@brandonsappliances.com
        </li>
        <li>
          <svg viewBox="0 0 24 24"><path d="M12 2a7 7 0 0 0-7 7c0 5 7 13 7 13s7-8 7-13a7 7 0 0 0-7-7zm0 9.5A2.5 2.5 0 1 1 12 6.5a2.5 2.5 0 0 1 0 5z"/></svg>
          148 Harbor View Rd, Millbrook, CT 06010
        </li>
      </ul>
    </div>
  </section>

  <section class="card card--back" aria-label="Business card back">
    <svg class="card__waves" viewBox="0 0 525 300" aria-hidden="true">
      <path class="wave" d="M0 0 H525 V115 C430 130 330 200 220 215 C140 225 60 225 0 215 Z"/>
    </svg>
    <div class="brand-name">Brandon's Appliances</div>
    <div class="website">WWW.BRANDONSAPPLIANCES.COM</div>
  </section>

</body>
</html>
```